Ember Ridge Clearing postcard ( for direct mailing) and business card design

Design postcards/Business cards
Dale Horvick
Ember Ridge Clearing
482 Copperfern Rd Alderbrook, ST 00000
(555) 555-0184 Dale@Emberridgeclearing.example

The postcard will be used for direct mailing to land owners and contractors to advertise our service. Pictures of the process and equipment along with a short summary of what we do. Business card should be contact info and logo.
Updates

The post cards could say something like this: Forestry Mulching machines are capable of clearing land of unwanted trees and brush with limited disturbance to soils or desirable vegetation. Traditional land clearing methods often present an increased risk of erosion by pushing over trees, uprooting the stump and roots, and substantially disturbing soils.In contrast, mulching the vegetation leaves the soil structure intact. The mulched material can be left on the ground and will act as an erosion barrier while returning nutrients back into the soil through decomposition. Over time, grass will naturally grow through the mulch and can be maintained with mowing.

Target Market(s)

Land owners and contractors who need vegetation cleared

Industry/Entity Type

Forestry Mulching

Requirements
Must have
• picture, brief description of service offered, contact info on postcard. Business card should have contact info and logo.
Nice to have
• I like contour lines as a background but I'd like to see other ideas.

```html
<!DOCTYPE html>
<html lang="en">
<head>
<meta charset="utf-8">
<title>Ember Ridge Clearing – Postcard</title>
<link rel="stylesheet" href="https://fonts.googleapis.com/css2?family=Montserrat:wght@400;500;600;700;800;900&display=swap">
<style>
:root{
  --green-dark:#1f7a34;
  --green:#23913d;
  --green-light:#8cc63f;
  --ink:#1c1c1c;
  --muted:#3a3a3a;
  --rule:#9a9a9a;
  --stamp:#e4e4e4;
  --page:#f2f2f2;
  --paper:#ffffff;
}
*{box-sizing:border-box;margin:0;padding:0}
html,body{width:800px;height:1200px;overflow:hidden}
body{background:var(--page);font-family:'Montserrat',sans-serif;color:var(--ink);position:relative}
.card{position:absolute;left:40px;width:720px;height:480px;background:var(--paper);box-shadow:0 2px 8px rgba(0,0,0,.18);overflow:hidden}
.card--front{top:70px}
.card--back{top:640px}
.card-art{position:absolute;inset:0}
.abs{position:absolute}

.brand{display:flex;align-items:center;gap:8px}
.brand-mark{width:14px;height:14px;background:var(--green-dark)}
.brand-name{font-weight:800;font-size:15px;line-height:15px;color:var(--ink);text-transform:uppercase;letter-spacing:.5px}

.headline{left:24px;top:84px;color:var(--green-dark);text-transform:uppercase}
.headline-main{font-weight:900;font-size:42px;line-height:40px;letter-spacing:.5px}
.headline-sub{font-weight:800;font-size:20px;line-height:22px}
.headline-tail{font-weight:500;font-size:17px;line-height:18px;color:var(--ink);letter-spacing:.6px}

.highlight-band{left:0;top:190px;width:342px;height:40px;background:var(--green-light);padding:7px 24px;font-size:10px;font-weight:500;line-height:13px;color:var(--ink)}

.uses{left:24px;top:240px;width:300px}
.uses-title{font-size:13px;font-weight:600;margin-bottom:6px}
.uses-title span{color:var(--green-dark)}
.uses-list{list-style:none}
.uses-list li{display:flex;align-items:flex-start;gap:6px;font-size:9px;font-weight:500;line-height:11px;margin-bottom:10px}
.uses-list svg{flex:none;width:15px;height:15px;margin-top:-2px}

.name-banner{height:26px;color:#fff;font-weight:800;text-transform:uppercase;display:flex;align-items:center}
.name-banner--front{left:24px;top:372px;width:222px;font-size:19px;padding-left:10px;background:var(--green-dark);clip-path:polygon(0 0,100% 0,92% 100%,0 100%)}
.call{font-weight:600;color:var(--ink)}
.call span{color:var(--green-light)}
.call--front{left:24px;top:402px;font-size:21px}
.contact{list-style:none;font-weight:500}
.contact li{display:flex;align-items:center;gap:7px}
.contact svg{flex:none}
.contact--front{left:24px;top:434px;font-size:11px}
.contact--front li{margin-bottom:8px}

.story{left:24px;top:262px;width:190px;font-size:8.2px;line-height:10.6px;text-align:justify;font-weight:500;color:var(--muted)}
.thumb{left:230px;width:100px;border:3px solid #fff;box-shadow:0 1px 4px rgba(0,0,0,.35)}
.thumb--one{top:260px;height:94px}
.thumb--two{top:370px;height:94px}
.name-back{left:24px;top:382px;font-size:18px;font-weight:800;color:var(--green-dark);text-transform:uppercase}
.call-bar{left:24px;top:404px;width:196px;height:20px;background:var(--green-light);font-size:14px;font-weight:600;display:flex;align-items:center;color:var(--ink)}
.call-bar span{color:#fff;background:var(--green-dark);height:100%;display:flex;align-items:center;padding:0 5px 0 6px;margin-right:5px}
.contact--back{left:24px;top:430px;font-size:8.5px}
.contact--back li{margin-bottom:3px}
.stamp{left:610px;top:40px;width:76px;height:76px;background:var(--stamp)}
.address-line{left:395px;width:290px;height:1px;background:var(--rule)}
</style>
</head>
<body>

<section class="card card--front" aria-label="Postcard front">
  <svg class="card-art" width="720" height="480" viewBox="0 0 720 480">
    <defs>
      <linearGradient id="frontPhoto" x1="0" y1="0" x2="0" y2="1">
        <stop offset="0" stop-color="#8fb3d9"/>
        <stop offset=".45" stop-color="#8a8470"/>
        <stop offset="1" stop-color="#3a3a28"/>
      </linearGradient>
    </defs>
    <polygon points="306,0 720,0 720,480 404,480" fill="url(#frontPhoto)" role="img" aria-label="Photo of a tracked loader with a forestry mulching head clearing brush"/>
    <polygon points="292,0 306,0 404,480 390,480" fill="var(--green)"/>
    <polygon points="630,0 720,0 720,200" fill="var(--green-light)" opacity=".55"/>
    <polygon points="272,480 404,480 384,350" fill="var(--green)"/>
  </svg>

  <div class="brand abs" style="left:24px;top:26px">
    <span class="brand-mark"></span>
    <span class="brand-name">Ember Ridge<br>Clearing</span>
  </div>

  <div class="headline abs">
    <div class="headline-main">Forestry</div>
    <div class="headline-sub">Mulching Machines</div>
    <div class="headline-tail">Are capable of clearing<br>land of unwanted trees</div>
  </div>

  <p class="highlight-band abs">Forestry Mulching is especially economical for smaller plots of land or areas with less access.</p>

  <div class="uses abs">
    <p class="uses-title"><span>When land</span> needs to be cleared</p>
    <ul class="uses-list">
      <li><svg viewBox="0 0 16 16"><circle cx="8" cy="8" r="7" fill="none" stroke="var(--green-dark)" stroke-width="1.2"/><path d="M5 8.2l2 2 4-4" fill="none" stroke="var(--green-dark)" stroke-width="1.4"/></svg>Adding roads</li>
      <li><svg viewBox="0 0 16 16"><circle cx="8" cy="8" r="7" fill="none" stroke="var(--green-dark)" stroke-width="1.2"/><path d="M5 8.2l2 2 4-4" fill="none" stroke="var(--green-dark)" stroke-width="1.4"/></svg>Servicing pipelines</li>
      <li><svg viewBox="0 0 16 16"><circle cx="8" cy="8" r="7" fill="none" stroke="var(--green-dark)" stroke-width="1.2"/><path d="M5 8.2l2 2 4-4" fill="none" stroke="var(--green-dark)" stroke-width="1.4"/></svg>Creating recreational spaces in a wooded area</li>
      <li><svg viewBox="0 0 16 16"><circle cx="8" cy="8" r="7" fill="none" stroke="var(--green-dark)" stroke-width="1.2"/><path d="M5 8.2l2 2 4-4" fill="none" stroke="var(--green-dark)" stroke-width="1.4"/></svg>Forestry mulching can be a very effective<br>method of clearing spaces</li>
    </ul>
  </div>

  <div class="name-banner name-banner--front abs">Dale Horvick</div>
  <p class="call call--front abs"><span>Call us:</span> (555) 555-0184</p>
  <ul class="contact contact--front abs">
    <li><svg width="9" height="11" viewBox="0 0 10 12"><path d="M5 0a4 4 0 0 0-4 4c0 3 4 8 4 8s4-5 4-8a4 4 0 0 0-4-4z" fill="var(--green-dark)"/><circle cx="5" cy="4" r="1.5" fill="#fff"/></svg>482 Copperfern Rd Alderbrook, ST 00000</li>
    <li><svg width="10" height="8" viewBox="0 0 10 8"><rect width="10" height="8" fill="var(--green-dark)"/><path d="M0 0l5 4 5-4" fill="none" stroke="#fff" stroke-width="1"/></svg>Dale@Emberridgeclearing.example</li>
  </ul>
</section>

<section class="card card--back" aria-label="Postcard back">
  <svg class="card-art" width="720" height="480" viewBox="0 0 720 480">
    <defs>
      <linearGradient id="backPhoto" x1="0" y1="0" x2="0" y2="1">
        <stop offset="0" stop-color="#9fb6c8"/>
        <stop offset=".5" stop-color="#6e6b62"/>
        <stop offset="1" stop-color="#55575a"/>
      </linearGradient>
    </defs>
    <rect x="0" y="0" width="360" height="250" fill="var(--green-dark)"/>
    <polygon points="70,0 355,0 305,250 20,250" fill="url(#backPhoto)" role="img" aria-label="Photo of the owner and his dog beside a tracked loader on a flatbed trailer"/>
    <polygon points="355,0 360,0 312,250 305,250" fill="var(--green-light)"/>
    <polygon points="20,250 30,250 80,0 70,0" fill="var(--green-light)" opacity=".8"/>
  </svg>

  <p class="story abs">Along with making space for planned projects, forestry mulching is also a great way to clear unwanted vegetation to allow more desirable food sources for local wildlife to flourish. Creating access to waterways that have become overgrown and clearing space for animals to gain new breeding grounds are other ways forestry mulching can be helpful</p>

  <div class="thumb thumb--one abs" role="img" aria-label="Photo of a mulching head working among bare trees" style="background:linear-gradient(#8c7b62,#4c3f30)"></div>
  <div class="thumb thumb--two abs" role="img" aria-label="Photo of a tractor with a mulcher in dark woods" style="background:linear-gradient(#2c2a26,#4a3a30)"></div>

  <p class="name-back abs">Dale Horvick</p>
  <p class="call-bar abs"><span>Call us:</span> (555) 555-0184</p>
  <ul class="contact contact--back abs">
    <li><svg width="7" height="9" viewBox="0 0 10 12"><path d="M5 0a4 4 0 0 0-4 4c0 3 4 8 4 8s4-5 4-8a4 4 0 0 0-4-4z" fill="var(--green-dark)"/><circle cx="5" cy="4" r="1.5" fill="#fff"/></svg>482 Copperfern Rd Alderbrook, ST 00000</li>
    <li><svg width="8" height="6" viewBox="0 0 10 8"><rect width="10" height="8" fill="var(--green-dark)"/><path d="M0 0l5 4 5-4" fill="none" stroke="#fff" stroke-width="1"/></svg>Dale@Emberridgeclearing.example</li>
    <li><svg width="7" height="7" viewBox="0 0 10 10"><circle cx="5" cy="5" r="5" fill="var(--green)"/></svg>www.Emberridgeclearing.example</li>
  </ul>

  <div class="brand abs" style="left:395px;top:48px">
    <span class="brand-mark"></span>
    <span class="brand-name">Ember Ridge<br>Clearing</span>
  </div>
  <div class="stamp abs"></div>
  <div class="address-line abs" style="top:262px"></div>
  <div class="address-line abs" style="top:292px"></div>
  <div class="address-line abs" style="top:322px"></div>
  <div class="address-line abs" style="top:352px"></div>
</section>

</body>
</html>
```